Redesign existing website

We would like a redesign of the website http://www.velbrisanalytics.com that creates a more modern, up to date look.

Velbris Analytics creates software for social science research and is focused on making the software user friendly and easy to use. We would like to convey seriousness, but also
a very up to date, just released look.

Feel free to modify the logo if you wish.

Target Market(s)

Academics, researchers

Industry/Entity Type

Software

Requirements
Must have
• The design should incorporate the same information as the current website.

```html
<!DOCTYPE html>
<html lang="en">
<head>
<meta charset="utf-8">
<title>Velbris Analytics</title>
<link rel="stylesheet" href="https://fonts.googleapis.com/css2?family=Arimo:wght@400;700&family=Didact+Gothic&family=Montserrat:wght@700&family=Cinzel:wght@600&display=swap">
<style>
  :root {
    --backdrop: #a9a9a9;
    --page: #ffffff;
    --navy: #16168c;
    --royal: #1c2a9c;
    --nav-bg: #d8e9fa;
    --nav-text: #3b6fae;
    --maroon: #7c1414;
    --bar-brown: #6d3232;
    --footer: #00007f;
    --ink: #222222;
    --gold: #f2c641;
  }
  * { box-sizing: border-box; margin: 0; padding: 0; }
  html, body { width: 1200px; height: 1135px; overflow: hidden; }
  body { background: var(--backdrop); position: relative; font-family: "Arimo", Arial, sans-serif; }
  .page {
    position: absolute; left: 121px; top: 65px; width: 937px; height: 1070px;
    background: var(--page); box-shadow: 4px 0 6px rgba(0,0,0,.35);
  }
  .abs { position: absolute; }
  .brand-mark { left: 49px; top: -42px; width: 138px; height: 138px; border-radius: 50%;
    background: var(--royal); border: 6px solid #c8ccd6; z-index: 2; }
  .divider-v { left: 232px; top: 0; width: 1px; height: 90px; background: #9a9a9a; }
  .divider-h { left: 0; top: 90px; width: 937px; height: 1px; background: #d0d0d0; }
  .brand-name { left: 254px; top: 38px; font-family: "Cinzel", Georgia, serif; font-weight: 600;
    font-size: 30px; line-height: 34px; color: var(--navy); white-space: nowrap; }
  .login { left: 756px; top: 38px; width: 156px; height: 39px; border: 2px solid #cfcfcf;
    font-family: "Didact Gothic", sans-serif; font-size: 19px; color: #777; text-align: center; line-height: 35px; letter-spacing: 1px; }
  .nav { left: 0; top: 121px; width: 232px; list-style: none; }
  .nav li { height: 37px; margin-bottom: 4px; background: var(--nav-bg);
    font-family: "Didact Gothic", sans-serif; font-size: 21px; color: var(--nav-text);
    padding-left: 52px; line-height: 37px; letter-spacing: 1.5px; }
  .mission { left: 254px; top: 116px; width: 505px; font-size: 16.5px; line-height: 19.5px; color: var(--navy); letter-spacing: .3px; }
  .mission p + p { margin-top: 10px; }
  .banner { left: 252px; top: 327px; width: 724px; height: 129px;
    background-image: linear-gradient(135deg, #2232a8, #17238f); }
  .banner-line { left: 296px; top: 369px; font-family: "Didact Gothic", sans-serif; font-size: 31px;
    line-height: 36px; color: #d8dcf0; letter-spacing: 2px; white-space: nowrap; }
  .news { left: 0; top: 405px; width: 234px; height: 392px; background: #fff;
    box-shadow: 3px 3px 5px rgba(0,0,0,.3); }
  .news-head { position: absolute; left: 0; top: 25px; width: 213px; height: 24px;
    background: linear-gradient(90deg, #8a5a1a, #c07a20); color: var(--gold);
    font-family: "Didact Gothic", sans-serif; font-size: 19px; text-align: right; padding-right: 4px; line-height: 24px; letter-spacing: 1px; }
  .news-title { position: absolute; left: 3px; top: 56px; width: 225px; font-weight: 700; font-size: 14px; line-height: 18px; color: #111; letter-spacing: .5px; }
  .news-body { position: absolute; left: 7px; top: 99px; width: 212px; font-size: 11px; line-height: 12.5px; color: var(--ink); letter-spacing: .5px; }
  .featured { left: 253px; top: 644px; font-family: "Montserrat", sans-serif; font-weight: 700;
    font-size: 38px; line-height: 44px; color: var(--maroon); letter-spacing: 1.5px; white-space: nowrap; }
  .product-bar { left: 253px; top: 722px; width: 660px; height: 37px; background: var(--bar-brown); }
  .product-name { left: 488px; top: 722px; line-height: 37px; font-family: "Didact Gothic", sans-serif;
    font-size: 25px; color: #fff; letter-spacing: 1.5px; }
  .product-shot { left: 293px; top: 700px; width: 177px; height: 123px;
    background: linear-gradient(160deg, #e9f0f8, #b9cde3); border: 1px solid #9fb3c8;
    box-shadow: 3px 3px 6px rgba(0,0,0,.35); }
  .product-intro { left: 488px; top: 781px; font-size: 14px; color: var(--navy); letter-spacing: .3px; }
  .features { left: 491px; top: 807px; width: 430px; list-style: none; font-size: 14px; line-height: 17px; color: var(--navy); letter-spacing: .3px; }
  .features li { position: relative; padding-left: 25px; margin-bottom: 11px; }
  .features svg { position: absolute; left: 0; top: 3px; }
  .preview { left: 254px; top: 971px; width: 154px; height: 38px; background: var(--bar-brown);
    border-top: 3px solid #b5b5b5; color: #fff; font-family: "Didact Gothic", sans-serif;
    font-size: 23px; line-height: 34px; padding-left: 25px; letter-spacing: 1.5px; }
  .footer { left: 0; top: 1036px; width: 937px; height: 34px; background: var(--footer);
    color: #fff; font-size: 13px; line-height: 34px; padding-left: 20px; letter-spacing: 1px; }
</style>
</head>
<body>
<div class="page">
  <div class="abs divider-v"></div>
  <div class="abs brand-mark"></div>
  <div class="abs divider-h"></div>
  <div class="abs brand-name">VELBRIS ANALYTICS</div>
  <div class="abs login">Login</div>

  <ul class="abs nav">
    <li>Home</li>
    <li>Products</li>
    <li>News</li>
    <li>About Us</li>
    <li>Contact Us</li>
  </ul>

  <div class="abs mission">
    <p>The mission of Velbris Analytics, Inc. is to produce software products that multiply the power and efficiency of empirical scientific research in the social sciences.</p>
    <p>A central goal is to expand access to complex data sources and to the advanced methods of scientific investigation needed to analyze them.</p>
  </div>

  <div class="abs banner" role="img" aria-label="Textured deep blue banner background"></div>
  <div class="abs banner-line">Empowering the social science researcher</div>

  <aside class="abs news">
    <div class="news-head">LATEST NEWS</div>
    <h3 class="news-title">New Approaches to Complex Data Management</h3>
    <p class="news-body">Technology such as StatPak and QuantSys used for retrieving and manipulating data has remained virtually unchanged since the first statistical packages were introduced almost four decades ago. In recent years, however, the scale and complexity of population and health data has expanded rapidly, and reliance on antiquated data management tools imposes heavy costs on the research community. This presentation will discuss new approaches to managing complex data and describe new technologies that will allow researchers to integrate and restructure complex data without custom programming.</p>
  </aside>

  <h2 class="abs featured">FEATURED PRODUCT</h2>
  <div class="abs product-bar"></div>
  <div class="abs product-name">Velbris Data Manager</div>
  <div class="abs product-shot" role="img" aria-label="Screenshot of the data manager application window"></div>
  <p class="abs product-intro">The Velbris Data Manager (VDM) helps researchers:</p>
  <ul class="abs features">
    <li><svg width="11" height="11" viewBox="0 0 11 11"><path d="M5.5 0L7 4 11 5.5 7 7 5.5 11 4 7 0 5.5 4 4Z" fill="#7a7fc4"/></svg>integrate data from different periods, places, and sources</li>
    <li><svg width="11" height="11" viewBox="0 0 11 11"><path d="M5.5 0L7 4 11 5.5 7 7 5.5 11 4 7 0 5.5 4 4Z" fill="#7a7fc4"/></svg>restructure complex data structures for analysis</li>
    <li><svg width="11" height="11" viewBox="0 0 11 11"><path d="M5.5 0L7 4 11 5.5 7 7 5.5 11 4 7 0 5.5 4 4Z" fill="#7a7fc4"/></svg>generate simple descriptive statistics for diagnostic purposes and feasibility analyses</li>
    <li><svg width="11" height="11" viewBox="0 0 11 11"><path d="M5.5 0L7 4 11 5.5 7 7 5.5 11 4 7 0 5.5 4 4Z" fill="#7a7fc4"/></svg>export subsets of variables and cases in formats suitable for analysis in any statistical package.</li>
  </ul>

  <div class="abs preview">Preview</div>
  <footer class="abs footer">Copyrite 2011</footer>
</div>
</body>
</html>
```